Zestra Design Prize - $10,000 tablet app design contest, Event App Category

Zestra is a marketplace for Kelo App Templates (similar to PageLoom templates). We want you to design an app template for sale in our marketplace which targets Event Apps (Kelo Apps that are created around music festivals, tradeshows, conferences or other events).

It’s up to you to create pages or features for the App Template that you think are appropriate. Creativity will be rewarded! Here are some example pages or features that you could create:

• A welcome page
• Event details – when and where?
• A location map
• A contact details page
• An event calendar (what’s on when?)
• Social media integration
• Video or animations

Your design should be Vibrant, Engaging and Contemporary. If you have an Kelo, download Zestra Viewer and download template examples in the download tab.

Your entry must include:
• A brief description of your template
• preview images of all pages of your template

Attached to this project are free templates to help you get started with your design. We have included:
1. A free portfolio template for designers/photographers
2. Icons and artwork to use in your template
3. Blank pages template
4. Form template
5. Video ad template

If you are selected as a finalist you will be required to submit an .oproject file containing:
• Your InDesign source files
• Preview images of your template
• All creative / stock assets used in the template (animations, video etc.)
• A text file with instructions on how to update the template
• A metadata .txt file containing template details and your information

How to enter:
1. Register at Marketplace and view the instructions under the welcome message https://marketplace.zestrahq.example/welcome
2. Download Zestra Editor: https://support.zestrahq.example/entries/58104963-zestra-editor
3. Use the free templates provided in this brief to create your designs and submit to ArtHively

Reason: Due to the Christmas break we are extending the deadline of our competition. Thank you for time and effort - I will be providing feedback over the next couple of days! Best wishes, Mirela

Hi All,

I have received many screenshots with some great designs! I just wanted to clarify that you are designing Zestra app templates including Zestra features and not just page designs?

Read Tips for First Time Zestrans to guide you through the template creation process

Before you start designing templates for Zestra Marketplace

·       Read the Quality Standards

·       Read the Copyright Information 

·       Use the Template Quality Checklist to ensure your template follows our guidelines. 

What should my project file contain?

·       A folder containing your source files, e.g. InDesign. This must be named Source.

·       The Zestra content files. This must be named Bundle.

·       Instructions, explaining to a customer how to use your template.

Best wishes,

Mirela

Reason: We are extending the competition by 7 days to give you more time!

Reason: Hello - we have received 3 entries for this contest so we are extending the deadline by 7 days. Best wishes, Mirela :)

Target Market(s)

Entrepreneurs who wish to create Kelo Apps by using our App design templates.

Industry/Entity Type

Events

Requirements
Must have
• You will need Zestra Editor to open the .oproject files attached to this brief. Get it here: https://support.zestrahq.example/entries/58104963-zestra-editor
Should not have
• Low quality, fuzzy or blurry images
- Any stock images or content which you do not own the rights to
- Any material which could be considered inappropriate or offensive

```html
<!DOCTYPE html>
<html lang="en">
<head>
<meta charset="utf-8">
<title>Zestra Event App – Menu</title>
<link rel="stylesheet" href="https://fonts.googleapis.com/css2?family=Michroma&display=swap">
<style>
  :root {
    --sky-deep: #1a66d8;
    --sky-mid: #2f8fec;
    --sky-light: #8ccbfb;
    --glow: #ffffff;
    --globe-light: #e9e3fb;
    --globe-mid: #c3bdf2;
    --globe-deep: #9aa3e8;
    --menu-text: #ffffff;
    --menu-shadow: #0a2870;
  }
  html, body {
    margin: 0;
    padding: 0;
    overflow: hidden;
    background: var(--sky-deep);
  }
  .app-screen {
    position: relative;
    width: 899px;
    height: 1200px;
    overflow: hidden;
  }
  .backdrop-art {
    position: absolute;
    inset: 0;
    background:
      radial-gradient(circle at 450px 600px, var(--glow) 0, rgba(255,255,255,0.9) 150px, rgba(255,255,255,0.35) 330px, rgba(255,255,255,0) 580px),
      radial-gradient(ellipse at 450px 600px, var(--sky-light) 0, var(--sky-mid) 45%, var(--sky-deep) 100%);
  }
  .globe-art {
    position: absolute;
    left: 309px;
    top: 452px;
    width: 276px;
    height: 276px;
    border-radius: 50%;
    background: radial-gradient(circle at 45% 40%, var(--globe-light) 0, var(--globe-mid) 60%, var(--globe-deep) 100%);
    opacity: 0.75;
  }
  .artwork {
    position: absolute;
    inset: 0;
  }
  .menu-item {
    font-family: "Michroma", "Arial Black", sans-serif;
    font-size: 26px;
    font-variant: small-caps;
    fill: var(--menu-text);
    stroke: var(--menu-text);
    stroke-width: 0.9px;
    filter: url(#menu-shadow);
  }
</style>
</head>
<body>
<main class="app-screen">
  <div class="backdrop-art" role="img" aria-label="Blue light-burst background artwork with bright white glow in the centre"></div>
  <div class="globe-art" role="img" aria-label="Illustrated glowing globe at the centre of the light burst"></div>
  <svg class="artwork" width="899" height="1200" viewBox="0 0 899 1200" xmlns="http://www.w3.org/2000/svg">
    <defs>
      <filter id="menu-shadow" x="-10%" y="-50%" width="120%" height="200%">
        <feDropShadow dx="2" dy="3" stdDeviation="1.8" flood-color="#0a2870" flood-opacity="0.8"/>
      </filter>
    </defs>
    <g class="main-menu">
      <text class="menu-item" x="263" y="215" textLength="94" lengthAdjust="spacingAndGlyphs">News</text>
      <text class="menu-item" x="555" y="273" textLength="223" lengthAdjust="spacingAndGlyphs">Information</text>
      <text class="menu-item" x="172" y="332" textLength="363" lengthAdjust="spacingAndGlyphs">Current Attendees</text>
      <text class="menu-item" x="225" y="390" textLength="537" lengthAdjust="spacingAndGlyphs">Performers/Speakers/Hosts</text>
      <text class="menu-item" x="145" y="448" textLength="145" lengthAdjust="spacingAndGlyphs">History</text>
      <text class="menu-item" x="582" y="507" textLength="146" lengthAdjust="spacingAndGlyphs">Gallery</text>
      <text class="menu-item" x="250" y="566" textLength="154" lengthAdjust="spacingAndGlyphs">Contact</text>
      <text class="menu-item" x="131" y="624" textLength="95" lengthAdjust="spacingAndGlyphs">Shop</text>
      <text class="menu-item" x="481" y="624" textLength="314" lengthAdjust="spacingAndGlyphs">Company Profile</text>
      <text class="menu-item" x="423" y="683" textLength="169" lengthAdjust="spacingAndGlyphs">Feedback</text>
      <text class="menu-item" x="105" y="741" textLength="687" lengthAdjust="spacingAndGlyphs">Confirm attendance/Make a Booking</text>
      <text class="menu-item" x="475" y="800" textLength="144" lengthAdjust="spacingAndGlyphs">SOCIAL</text>
      <text class="menu-item" x="211" y="858" textLength="162" lengthAdjust="spacingAndGlyphs">Location</text>
      <text class="menu-item" x="288" y="917" textLength="367" lengthAdjust="spacingAndGlyphs">Timetable/Calendar</text>
    </g>
  </svg>
</main>
</body>
</html>
```